2367 Halvorsen Avenue Medical Centre

We are looking for a design for new medical clinic.
We are accepting new patients at this new medical centre grand opening. Walk-ins are welcome.
Our cardiac and vascular surgical specialists are department heads at St Alder's Hospital, a leading teaching hospital in Toronto. These specialists will see cardiovascular consults are well as pre-surgical and post-surgical consultations and follow-ups.
Our lab is affiliated with several nuclear medicine clinics in the GTA.
Our Services Includes:
Family Practice
Cardiology Diagnostics
Cardiac & Vascular Surgical Consultation
Ultrasound & Vascular Testing
Open 6 days a week.
Ample Free Parking
Friendly Staffs

Target Market(s)

New Patients. Families of any age. Ethnic groups including Asians & Africans.

Industry/Entity Type

Medical

Font styles to use
Serif
Sans Serif
Decorative
Script
Other font styles liked:
• Arial calibri, verdana

Requirements
Must have
• Address:
• 2367 Halvorsen Avenue East
• Unit 418
• Brackenford, Ontario
• K7T 2P4
• Tel: (416) 555-0148
Nice to have
• Caring and inviting environment.
• Simple but classy.
• Standout colors.
Should not have
• Busy images. Aside from this, any ideas are welcome.

```html
<!DOCTYPE html>
<html lang="en">
<head>
<meta charset="utf-8">
<title>2367 Halvorsen Avenue Medical Centre – Now Open</title>
<link href="https://fonts.googleapis.com/css2?family=Arimo:wght@700&display=swap" rel="stylesheet">
<style>
  :root {
    --ink: #0a0a0a;
    --sky: #29abe2;
    --sky-deep: #1c7fc4;
    --sky-pale: #bfe3f5;
    --steel: #8c8f93;
    --mist: #eef2f5;
    --bar: rgba(214, 218, 222, 0.85);
  }
  html, body { margin: 0; padding: 0; overflow: hidden; background: #fff; }
  .flyer {
    position: relative;
    width: 927px;
    height: 1200px;
    overflow: hidden;
    background: var(--mist);
    font-family: "Arimo", Arial, sans-serif;
    font-weight: 700;
    color: var(--ink);
  }
  .hero-photo {
    position: absolute; left: 0; top: 0; width: 927px; height: 420px;
    background:
      linear-gradient(90deg, rgba(41,171,226,0.55) 0%, rgba(230,240,246,0.7) 14%, rgba(244,247,250,0.9) 45%, rgba(236,242,247,0.9) 62%, rgba(33,99,196,0.95) 82%, rgba(45,110,205,1) 100%);
  }
  .backdrop-photo {
    position: absolute; left: 0; top: 360px; width: 927px; height: 840px;
    background: linear-gradient(180deg, #eef2f5 0%, #f3f5f7 40%, #e9eef2 100%);
  }
  .shapes { position: absolute; inset: 0; }
  .booking-bar {
    position: absolute; left: 0; top: 0; width: 612px; height: 57px;
    background: var(--bar);
  }
  .booking-bar p {
    margin: 0; position: absolute; left: 23px; top: 18px;
    font-size: 20.5px; line-height: 1; white-space: nowrap;
  }
  .headline { position: absolute; margin: 0; line-height: 1; white-space: nowrap; }
  .headline--clinic { left: 73px; top: 103px; font-size: 45.5px; }
  .headline--days { left: 187px; top: 163px; font-size: 36px; }
  .headline--walkin { left: 105px; top: 492px; font-size: 45.5px; }
  .services { position: absolute; left: 52px; top: 662px; }
  .services h2 { margin: 0 0 17px; font-size: 36px; line-height: 1; white-space: nowrap; }
  .services ul { list-style: none; margin: 0; padding: 0; }
  .services li { font-size: 27px; line-height: 1; height: 52px; margin-left: 1px; white-space: nowrap; }
  .address {
    position: absolute; left: 499px; top: 964px;
    font-size: 24px; line-height: 29px; margin: 0; font-style: normal; white-space: nowrap;
  }
</style>
</head>
<body>
<main class="flyer">
  <div class="backdrop-photo" role="img" aria-label="Soft faded photo of a doctor in a white coat holding a clipboard and pen"></div>
  <div class="hero-photo" role="img" aria-label="Photo of a doctor in blue scrubs with arms crossed in a bright hospital room"></div>

  <svg class="shapes" width="927" height="1200" viewBox="0 0 927 1200" aria-hidden="true">
    <path d="M0 470 C120 390 260 350 380 355 C560 362 720 395 927 395 L927 445 C760 420 560 380 360 372 C220 368 100 420 0 500 Z" fill="var(--sky)"/>
    <path d="M360 372 C560 380 760 420 927 445 L927 445 C760 440 560 420 430 388 Z" fill="var(--steel)"/>
    <path d="M0 500 C100 420 220 368 360 372 C260 380 150 430 80 500 C40 540 10 590 0 620 Z" fill="var(--sky)"/>
    <path d="M927 478 L634 764 L927 1054 Z" fill="var(--steel)"/>
    <path d="M927 493 L667 764 L927 1042 Z" fill="var(--sky)"/>
    <path d="M0 1160 C200 1115 420 1110 600 1130 C740 1145 850 1150 927 1140 L927 1200 L0 1200 Z" fill="var(--sky-pale)"/>
    <path d="M0 1175 C180 1130 400 1128 580 1148 C720 1163 840 1168 927 1160 L927 1200 L0 1200 Z" fill="var(--sky-deep)"/>
  </svg>

  <div class="booking-bar"><p>TO BOOK APPOINTMENT, PLEASE CALL (416) 555-0148</p></div>

  <h1 class="headline headline--clinic">NEW MEDICAL CLINIC</h1>
  <p class="headline headline--days">OPEN 6 DAYS A WEEK.</p>
  <p class="headline headline--walkin">ACCEPTING WALK-IN PATIENTS.</p>

  <section class="services">
    <h2>SERVICES INCLUDES</h2>
    <ul>
      <li>Family Practice</li>
      <li>Cardiology Diagnostics</li>
      <li>Cardiac &amp; Vascular Surgical Consultation</li>
      <li>Ultrasound &amp; Vascular</li>
    </ul>
  </section>

  <address class="address">
    ADDRESS:<br>
    2367 Halvorsen Avenue East<br>
    Unit 418<br>
    Brackenford, Ontario<br>
    K7T 2P4
  </address>
</main>
</body>
</html>
```